Design for a real estate wev portal

Contents and features of the site
---------------------------------
Website in 5 languages: French, Dutch, English, German, Spanish.
English name of the site: Lantern Nest Living
Main purpose of the site:
- allow people to rent their house/ appartment for flatsharing purposes.
- help people wanting to find a room in flatsharing
- help people to find additional roommates for their flatsharing
Key interaction sequence:
1. I create a "group" of people who have common interest/hobbies
2. People who have the same interests/hobbies join my group
3. I look for a house/appartment to host my group
Website structure will be the following:
- Home
- Groups
-- Look for a group
--- Join a group
-- Create a group
- Properties
-- Look for a house/appartement
-- Apply
- Sales conditions
- Contact
- My account
-- My profile
-- My groups OR my properties
Your mission
------------
The client has no graphical guidelines, simply a logo (see attached).
We need a (responsive compliant) design for the following pages (we expect PSD's from you. No HTML nor CSS):
1. homepage (see example and wireframe attached)
2. properties search result list (see wireframe attached)
3. "detailed" form for properties
4. groups search result list
5. "detailed" form for groups
6. my account page
FOR THE COMPETITION step we only expect from you the design of first 2 screens.
Based on that, we will select the designer who will win the project, and will have to design the 4 remaining screens.
Target Market(s)
B2C
Industry/Entity Type
Real Estate
Number of Pages Required
5+ page
Look and feel
Each slider illustrates characteristics of the customer's brand and the style your logo design should communicate.

```html
<!DOCTYPE html>
<html lang="en">
<head>
<meta charset="utf-8">
<title>Lantern Nest Living — Home</title>
<link rel="stylesheet" href="https://fonts.googleapis.com/css2?family=Open+Sans:wght@400;600;700&display=swap">
<style>
:root{
  --green:#6abf3e;
  --green-dark:#5aa932;
  --teal:#1897a8;
  --teal-text:#2f9fb2;
  --ink:#222;
  --muted:#777;
  --line:#cfcfcf;
  --panel:#f1f1f1;
  --footer:#f3f3f3;
  --dark-btn:#333;
}
*{box-sizing:border-box;margin:0;padding:0}
html,body{width:1200px;height:2308px;overflow:hidden}
body{font-family:"Open Sans",Arial,sans-serif;color:var(--ink);background:#fff;position:relative}
.abs{position:absolute}
/* header */
.site-header{position:absolute;left:0;top:0;width:1200px;height:157px;background:#fff}
.main-nav{position:absolute;left:132px;top:108px;display:flex;gap:25px;font-size:13px}
.main-nav a{color:#222;text-decoration:none;position:relative}
.main-nav a.active{color:var(--green)}
.main-nav a.active::before{content:"";position:absolute;left:8px;top:-17px;width:10px;height:9px;background:var(--green);clip-path:polygon(50% 0,100% 50%,85% 50%,85% 100%,15% 100%,15% 50%,0 50%)}
.brand{position:absolute;left:495px;top:58px;width:215px;display:flex;align-items:center;gap:8px;font-size:21px;font-weight:700;color:#333;line-height:1}
.brand .dot{width:16px;height:16px;border-radius:50%;background:var(--green);flex:none}
.account-link{position:absolute;right:133px;top:54px;font-size:10px;color:#333}
.account-tools{position:absolute;right:133px;top:88px;display:flex;gap:17px}
.tool-btn{height:35px;border:1px solid #bbb;font-size:11px;padding:0 12px;display:flex;align-items:center;gap:6px;color:#333}
/* hero */
.hero{position:absolute;left:0;top:157px;width:1200px;height:456px;background:linear-gradient(100deg,#5a4a3e 0%,#b9a898 30%,#e4d6c6 50%,#c7b7a6 70%,#6d6058 100%)}
.hero-arrow{position:absolute;top:210px;width:20px;height:36px}
.choice-panel{position:absolute;top:200px;width:398px;height:228px;background:rgba(255,255,255,.93);text-align:center}
.choice-panel h2{font-weight:400;font-size:21px;margin-top:15px;color:#333}
.choices{display:flex;gap:14px;justify-content:center;margin-top:20px}
.choice{width:180px;height:147px;border:1px solid #aaa;display:flex;flex-direction:column;align-items:center;padding-top:24px;font-size:14px;line-height:1.4;color:#333}
.choice svg{margin-bottom:14px}
.choice.active{border:2px solid var(--green);color:var(--green)}
/* listings */
.listing{position:absolute;width:455px;height:160px;background:var(--panel);display:flex}
.listing .photo{width:160px;height:160px;flex:none}
.listing .info{padding:14px 0 0 22px}
.listing h3{font-size:16px;font-weight:400;color:var(--teal-text)}
.listing .lead{font-size:11.5px;margin-top:8px;line-height:1.45;font-weight:600;color:#222}
.listing .meta{font-size:9.5px;color:#666;margin-top:6px;line-height:1.9}
.btn-green{display:inline-block;background:var(--green);color:#fff;font-size:9.5px;font-weight:700;padding:7px 11px;margin-top:10px;letter-spacing:.3px}
.btn-more{position:absolute;top:1045px;width:160px;height:34px;background:#e6e6e6;font-size:9.5px;color:#666;display:flex;align-items:center;justify-content:center;letter-spacing:.3px}
/* selling */
.selling{position:absolute;left:0;top:1144px;width:1200px;height:358px;background:linear-gradient(90deg,#5d5a55,#8d8881 45%,#a29c93 70%,#4f4b47)}
.selling h2{position:absolute;top:42px;width:100%;text-align:center;color:#fff;font-size:28px;font-weight:700}
.point{position:absolute;top:95px;width:455px;height:174px;background:#fff;padding:28px 28px}
.point .lead{font-size:13px;line-height:1.5}
.point .body{font-size:9.5px;color:#999;line-height:1.6;margin-top:10px}
.point .read{font-size:9.5px;color:var(--green);margin-top:14px}
.dots{position:absolute;top:302px;left:558px;display:flex;gap:16px}
.dots i{width:8px;height:8px;border-radius:50%;background:#ccc}
.dots i.on{background:var(--green)}
/* faq */
.faq-title{position:absolute;top:1573px;width:100%;text-align:center;font-size:29px;font-weight:700;color:var(--green)}
.faq-q{position:absolute;left:132px;width:935px;height:43px;border:1px solid var(--line);font-size:14.5px;display:flex;align-items:center;padding-left:22px;gap:10px}
.faq-q .chev{position:absolute;right:20px;top:15px}
.qmark{width:14px;height:14px;border-radius:50%;background:#222;color:#fff;font-size:10px;font-weight:700;display:flex;align-items:center;justify-content:center}
.faq-a{position:absolute;left:132px;top:1677px;width:935px;height:101px;background:#f4f4f4;padding:18px 22px 0 48px;font-size:11px;color:#999;line-height:1.7}
.faq-a::before{content:"i";position:absolute;left:22px;top:20px;width:13px;height:13px;border-radius:50%;background:#bbb;color:#fff;font-size:9px;text-align:center;line-height:13px;font-weight:700}
.faq-a b{color:var(--teal-text);font-weight:400}
/* bottom bands */
.searches{position:absolute;left:0;top:1974px;width:600px;height:240px;background:var(--green);padding:22px 0 0 130px}
.tools{position:absolute;left:600px;top:1974px;width:600px;height:240px;background:var(--teal);padding:22px 0 0 26px;color:#fff}
.band-title{font-size:28px;font-weight:600;color:#fff}
.field-grid{display:grid;grid-template-columns:218px 220px;gap:9px 10px;margin-top:22px}
.field{height:39px;background:#fff;font-size:11.5px;color:#444;display:flex;align-items:center;padding:0 16px;justify-content:space-between}
.btn-search{margin-top:9px;width:92px;height:39px;background:var(--dark-btn);color:#fff;font-size:13px;font-weight:700;display:flex;align-items:center;justify-content:center}
.tool-list{display:grid;grid-template-columns:256px 200px;row-gap:10px;margin-top:26px;font-size:12px}
.tool-list span{display:flex;align-items:center;gap:12px}
.tool-list span::before{content:"";width:10px;height:10px;background:#fff;border-radius:2px}
/* footer */
.site-footer{position:absolute;left:0;top:2214px;width:1200px;height:94px;background:var(--footer)}
.footer-nav{position:absolute;left:132px;top:28px;font-size:11px;color:#333;word-spacing:2px}
.copyright{position:absolute;left:132px;top:56px;font-size:11px;color:#333}
.social{position:absolute;left:847px;top:30px;display:flex;gap:6px}
.social i{width:26px;height:26px;border-radius:50%;background:#1d4d80}
</style>
</head>
<body>

<header class="site-header">
  <nav class="main-nav">
    <a class="active">Home</a><a>Services</a><a>Areas</a><a>Reviews</a><a>Contact</a>
  </nav>
  <div class="brand"><span class="dot"></span>Lantern Nest Living</div>
  <div class="account-link">&#9679; My Account</div>
  <div class="account-tools">
    <div class="tool-btn"><svg width="14" height="9"><rect width="14" height="9" fill="#c33"/><rect y="3" width="14" height="3" fill="#fff"/></svg>English &#8964;</div>
    <div class="tool-btn">&#128274;&#xFE0E; Log in</div>
    <div class="tool-btn">&#9998; Register</div>
  </div>
</header>

<section class="hero" role="img" aria-label="Photo of three young flatmates laughing together in a bright kitchen">
  <svg class="hero-arrow" style="left:24px" viewBox="0 0 20 36"><path d="M17 2 3 18l14 16" fill="none" stroke="#fff" stroke-width="3" opacity=".7"/></svg>
  <svg class="hero-arrow" style="right:24px" viewBox="0 0 20 36"><path d="M3 2l14 16L3 34" fill="none" stroke="#fff" stroke-width="3" opacity=".7"/></svg>

  <div class="choice-panel" style="left:188px">
    <h2>Searching for accommodation</h2>
    <div class="choices">
      <div class="choice active">
        <svg width="56" height="46" viewBox="0 0 56 46" fill="none" stroke="#6abf3e" stroke-width="2"><path d="M4 22 28 3l24 19M10 18v26h36V18M23 44V30h10v14M40 8v8"/></svg>
        I want to rent a room<br>right now !
      </div>
      <div class="choice">
        <svg width="90" height="46" viewBox="0 0 90 46" fill="none" stroke="#555" stroke-width="1.6"><circle cx="45" cy="14" r="9"/><path d="M30 44c0-12 7-18 15-18s15 6 15 18"/><circle cx="20" cy="18" r="7"/><path d="M6 44c0-10 6-15 14-15 4 0 7 1 9 3"/><circle cx="70" cy="18" r="7"/><path d="M84 44c0-10-6-15-14-15-4 0-7 1-9 3"/></svg>
        I want to<br>join a group
      </div>
    </div>
  </div>

  <div class="choice-panel" style="left:611px">
    <h2>I have a house for rent</h2>
    <div class="choices">
      <div class="choice">
        <svg width="56" height="46" viewBox="0 0 56 46" fill="none" stroke="#555" stroke-width="1.8"><path d="M6 17h10l24-12v36L16 29H6zM16 17v12M40 5h6v36h-6M12 29l4 14h6l-3-14"/></svg>
        I want to<br>advertise !
      </div>
      <div class="choice">
        <svg width="50" height="50" viewBox="0 0 50 50" fill="none" stroke="#555" stroke-width="1.8"><circle cx="25" cy="25" r="22"/><path d="M19 19c0-4 3-6 6-6s6 2 6 6c0 5-6 5-6 10"/><circle cx="25" cy="35" r="1" fill="#555"/></svg>
        Why is flatsharing<br>interesting for me ?
      </div>
    </div>
  </div>
</section>

<article class="listing" style="left:132px;top:679px">
  <div class="photo" role="img" aria-label="Photo of young workers chatting in a living room" style="background:linear-gradient(135deg,#c9b9a2,#7a6450)"></div>
  <div class="info">
    <h3>Maecenas tempus, tortor</h3>
    <p class="lead">Young workers, seeking for accomodation<br>downtown.</p>
    <p class="meta">Average age : 35 Men and women welcome</p>
    <span class="btn-green">JOIN TO THIS GROUP</span>
  </div>
</article>
<article class="listing" style="left:611px;top:679px">
  <div class="photo" role="img" aria-label="Photo of a bright furnished living room" style="background:linear-gradient(135deg,#e7e4de,#9b8a78)"></div>
  <div class="info">
    <h3>House name</h3>
    <p class="lead">24 Building name, Street name, City - Zipcode</p>
    <p class="meta">Rent Per Month : $000<br>Availability : 2</p>
    <span class="btn-green">VIEW THIS HOUSE</span>
  </div>
</article>
<article class="listing" style="left:132px;top:862px">
  <div class="photo" role="img" aria-label="Photo of friends cooking and sharing a meal" style="background:linear-gradient(135deg,#a88d74,#4f3b30)"></div>
  <div class="info">
    <h3>Maecenas tempus, tortor</h3>
    <p class="lead">Young workers, seeking for accomodation<br>downtown.</p>
    <p class="meta">Average age : 35 Men and women welcome</p>
    <span class="btn-green">JOIN TO THIS GROUP</span>
  </div>
</article>
<article class="listing" style="left:611px;top:862px">
  <div class="photo" role="img" aria-label="Photo of an open living room with staircase" style="background:linear-gradient(135deg,#ddd6cc,#8a6f55)"></div>
  <div class="info">
    <h3>Maecenas tempus, tortor</h3>
    <p class="lead">24 Building name, Street name, City - Zipcode</p>
    <p class="meta">Rent Per Month : $000<br>Availability : 2</p>
    <span class="btn-green">VIEW THIS HOUSE</span>
  </div>
</article>
<div class="btn-more" style="left:132px">SEE MORE GROUPS &nbsp;&#187;</div>
<div class="btn-more" style="left:611px">SEE MORE HOUSES &nbsp;&#187;</div>

<section class="selling" role="img" aria-label="Photo of a modern living room interior in grey tones">
  <h2>KEY SELLING POINTS FOR THE ROOMMATES</h2>
  <div class="point" style="left:132px">
    <p class="lead">Suspendisse sagittis facilisis est quis vulputate. Mauris suscipit tellus eu metus egestas aliquet. Pellentesque at leo tellus.</p>
    <p class="body">Curabitur mi sem, ullamcorper accumsan finibus vel, facilisis eget dolor. Integer rhoncus ligula at tempor ultrices. Vestibulum sollicitudin congue arcu, et pharetra ligula hendrerit et. Fusce blandit facilisis neque sed ornare. Etiam eget scelerisque dolor.</p>
    <p class="read">READ MORE</p>
  </div>
  <div class="point" style="left:611px">
    <p class="lead">Suspendisse sagittis facilisis est quis vulputate. Mauris suscipit tellus eu metus egestas aliquet. Pellentesque at leo tellus.</p>
    <p class="body">Curabitur mi sem, ullamcorper accumsan finibus vel, facilisis eget dolor. Integer rhoncus ligula at tempor ultrices. Vestibulum sollicitudin congue arcu, et pharetra ligula hendrerit et. Fusce blandit facilisis neque sed ornare. Etiam eget scelerisque dolor.</p>
    <p class="read">READ MORE</p>
  </div>
  <div class="dots"><i class="on"></i><i></i><i></i><i></i></div>
</section>

<h2 class="faq-title">EVERYTHING YOU NEED TO KNOW ABOUT FLATSHARING</h2>
<div class="faq-q" style="top:1635px"><span class="qmark">?</span>Phasellus semper libero sed erat facilisis pellentesque sit amet quis orci?
  <svg class="chev" width="12" height="8"><path d="M1 7l5-5 5 5" fill="none" stroke="#555" stroke-width="1.3"/></svg></div>
<div class="faq-a">Suspendisse sagittis facilisis est quis vulputate. Mauris suscipit tellus eu metus egestas aliquet. Pellentesque at leo tellus. Suspendisse potenti. Fusce efficitur, mi vel dictum elementum, massa lorem suscipit libero, eu dictum mauris ligula sit amet lectus. Donec blandit metus sit amet dolor consequat hendrerit. Phasellus sollicitudin interdum risus, in viverra erat luctus sed. Curabitur rutrum ac nulla at elementum. <b>More</b></div>
<div class="faq-q" style="top:1795px"><span class="qmark">?</span>Curabitur mi sem, ullamcorper accumsan finibus vel, facilisis eget?
  <svg class="chev" width="12" height="8"><path d="M1 1l5 5 5-5" fill="none" stroke="#555" stroke-width="1.3"/></svg></div>
<div class="faq-q" style="top:1851px"><span class="qmark">?</span>Quisque molestie ligula id diam tincidunt, sed porttitor neque rutrum?
  <svg class="chev" width="12" height="8"><path d="M1 1l5 5 5-5" fill="none" stroke="#555" stroke-width="1.3"/></svg></div>

<section class="searches">
  <h2 class="band-title">Pre-Defined Searches</h2>
  <div class="field-grid">
    <div class="field">Location, Area, Zipcode <span>&#9906;</span></div>
    <div class="field">Rent Range <span>&#8964;</span></div>
    <div class="field">Room Type <span>&#8964;</span></div>
    <div class="field">Members Count <span>&#8964;</span></div>
  </div>
  <div class="btn-search">SEARCH</div>
</section>

<section class="tools">
  <h2 class="band-title">Tools and Informations</h2>
  <div class="tool-list">
    <span>Maecenas tempus</span><span>Maecenas tempus</span>
    <span>Phasellus sollicitudin interdu</span><span>Phasellus sollicitudin interdu</span>
    <span>Curabitur mi sem</span><span>Curabitur mi sem</span>
    <span>Etiam eget</span><span>Etiam eget</span>
    <span>Quisque molestie</span><span>Quisque molestie</span>
  </div>
</section>

<footer class="site-footer">
  <p class="footer-nav">Home &nbsp;| &nbsp;Services &nbsp;| &nbsp;Areas &nbsp;| &nbsp;Reviews &nbsp;| &nbsp;Contact &nbsp;| &nbsp;Terms and Conditions &nbsp;| &nbsp;Privacy Policy</p>
  <p class="copyright">Copyright &copy; 2016 Company name. All rights reserved.</p>
  <div class="social" aria-label="Social links"><i></i><i></i><i></i><i></i><i></i><i></i><i></i></div>
</footer>

</body>
</html>
```